EILT: Landing Page - EXPRESS VERSAND
Zielgruppe
Es soll in kurzer Zeit (max 48 Stunden) eine kleine Ladingpage entstehen. Expressversand / Import von China nach Deutschland . Aufgrund der stark steigenden Luftfrachtraten aus China heraus hat sich unsere Firma Fracht-Kapazitäten gesichert. Diese sollen nun angeboten werden. Über eine Ladingpage sollen Anfragen generiert werden. Diese Anfragen werden dann mit einem Angebot von uns beantwortet. Expressversand / Import von China nach Deutschland
Aufgabenstellung
Die Seite soll beinhalten:
- 1-2 Bilder (z. B. Luftfracht, Logistik, Flugzeug, Cargo, etc)
- kurzer erklärender Text: z.B. 'jetzt Angebot anfordern und günstig aus China per Express versenden.' Inkl. Abholung, Verzollung und Zustellung. Kurze Laufzeit von nur 3-5 Tagen. ab 45€ / Paket
- Anfrage Formular, bestehend aus: , Abholadresse in China/Post Code, ZielAdresse Deutschland, Sendungsinformationen (wie viele Kartons, wie schwer ist ein Karton und welche Abmessungen L/B/H ), wann ist die Sendung in China abholbereit, optional: Sendungsinhalt (Ware, Zolltarifnummer/HS Code) , Firma, Name, email adresse
- optional ein Header/Laufband etc mit: Bis zum 19. Nov 21 versenden - Ware bis MegaSonntag erhalten!
- 24h Servicehotline, Tel: 0987/314265
- 2-3 Kundenreferenzen: Bilder von Personen mit Text : „Schneller Versand - nur 4 Tage Laufzeit“ , „1A Service, ohne Probleme“ , „gute Preise - nur zu empfehlen.“
Unser Firmenlogo kann - muss aber nicht auftauchen.
In der farblichen Gestaltung haben Sie freie Hand und freuen uns auf Ihre Vorschläge.
Aufgrund der Dringlichkeit sollte diese Landingpage innerhalb 48 Stunden 'live ' gehen.
WICHTIG: Die Page sollte von Ihnen auch veröffentlich werden. Aktuell nutzen wir den Kelvo Homepagebaukasten. Die Page kann aber auch durch andere Anbieter veröffentlicht werden , zb Pagerune

```html
<!DOCTYPE html>
<html lang="de">
<head>
<meta charset="utf-8">
<title>Expressversand China – Deutschland</title>
<link href="https://fonts.googleapis.com/css2?family=Source+Sans+3:wght@400;600;700&display=swap" rel="stylesheet">
<style>
:root{
  --purple:#7a1fe0;
  --red:#cf4a3a;
  --white:#ffffff;
  --ink:#1c1c1c;
  --quote:#c9c2c0;
  --star:#f6b53a;
}
*{box-sizing:border-box;margin:0;padding:0}
html,body{width:1200px;height:816px;overflow:hidden;background:var(--white);font-family:"Source Sans 3",sans-serif}
.page{position:relative;width:1200px;height:816px}
.promo-bar{position:absolute;left:0;top:0;width:1200px;height:53px;display:flex;align-items:center;justify-content:center;color:var(--purple);font-weight:600;font-size:20px;background:var(--white)}
.hero{position:absolute;left:0;top:53px;width:1200px;height:714px;overflow:hidden}
.hero-photo{position:absolute;inset:0;background:linear-gradient(180deg,#7c5a55 0%,#b9714c 30%,#9c6a4c 55%,#5a4a45 80%,#3e3a3c 100%)}
.hero-photo::after{content:"";position:absolute;inset:0;background:radial-gradient(ellipse at 85% 40%,rgba(240,170,80,.45),transparent 60%)}
.brand{position:absolute;left:154px;top:14px;display:flex;align-items:center;gap:10px;color:var(--white);font-weight:700;font-size:26px}
.brand-dot{width:44px;height:44px;border-radius:50%;background:var(--red)}
.headline{position:absolute;left:150px;top:154px;color:var(--white);font-weight:700;font-size:43px;line-height:43px}
.hotline-label{position:absolute;left:185px;top:342px;color:var(--white);font-weight:600;font-size:26px}
.hotline{position:absolute;left:154px;top:377px;width:275px;height:46px;border-radius:23px;background:var(--red);display:flex;align-items:center;padding-left:24px;gap:10px;color:var(--white);font-weight:700;font-size:29px}
.request-form{position:absolute;left:603px;top:44px;width:447px;height:390px;background:linear-gradient(120deg,var(--purple) 0%,#a32fb0 50%,#c9453c 100%)}
.form-intro{position:absolute;left:19px;top:13px;width:420px;color:var(--white);font-weight:600;font-size:14.5px;line-height:19.5px}
.field{position:absolute;width:202px;height:37px;background:var(--white);border:none;padding-left:14px;font-family:inherit;font-size:12.5px;color:var(--ink)}
.field::placeholder{color:var(--ink)}
.send-btn{position:absolute;left:110px;top:332px;width:230px;height:40px;border:2px solid var(--white);border-radius:20px;background:var(--red);color:var(--white);font-family:inherit;font-weight:600;font-size:17px;display:flex;align-items:center;justify-content:center;gap:12px}
.quote-mark{position:absolute;left:148px;top:470px;color:var(--quote);font-weight:700;font-size:150px;line-height:1;opacity:.85}
.reviews-title{position:absolute;left:0;top:495px;width:1200px;text-align:center;color:var(--white);font-weight:600;font-size:27px}
.review{position:absolute;top:557px;width:289px;height:125px;background:rgba(207,74,58,.85);color:var(--white)}
.review-text{margin-top:16px;text-align:center;font-size:15px}
.reviewer{position:absolute;top:51px;display:flex;align-items:center;gap:8px}
.avatar{width:54px;height:54px;border-radius:50%;background:linear-gradient(135deg,#6b4a3c,#2b2322)}
.reviewer-name{font-size:12.5px}
.stars{color:var(--star);font-size:11px;letter-spacing:1px}
.footer{position:absolute;left:0;top:767px;width:1200px;height:49px;display:flex;align-items:center;justify-content:center;font-size:12.5px;color:var(--ink)}
</style>
</head>
<body>
<div class="page">
  <div class="promo-bar">noch bis 19. November versenden und Sendung bis MegaSonntag herhalten!</div>
  <section class="hero">
    <div class="hero-photo" role="img" aria-label="Frachtflugzeug, Containerschiff und Lkw im Hafen bei Sonnenuntergang"></div>
    <div class="brand"><span class="brand-dot"></span>Frachtwerk</div>
    <h1 class="headline">Expressversand /<br>Import von China<br>nach Deutschland</h1>
    <div class="hotline-label">24h Servicehotline</div>
    <div class="hotline">
      <svg width="26" height="26" viewBox="0 0 24 24" fill="none" stroke="#fff" stroke-width="1.8"><path d="M5 3h4l2 5-2.5 1.5a11 11 0 0 0 6 6L16 13l5 2v4a2 2 0 0 1-2 2A17 17 0 0 1 3 5a2 2 0 0 1 2-2z"/><path d="M14 3a7 7 0 0 1 7 7M14 7a3 3 0 0 1 3 3"/></svg>
      0987/314265
    </div>
    <form class="request-form">
      <p class="form-intro">Jetzt Angebot anfordern und günstig aus China per Express versenden.' Inkl. Abholung, Verzollung und Zustellung. Kurze Laufzeit von nur 3-5 Tagen. ab 45€ / Paket</p>
      <input class="field" style="left:17px;top:91px" placeholder="Firma">
      <input class="field" style="left:229px;top:91px" placeholder="Name">
      <input class="field" style="left:18px;top:138px" placeholder="Email Adresse">
      <input class="field" style="left:230px;top:138px" placeholder="Abholadresse in China">
      <input class="field" style="left:20px;top:184px" placeholder="Post Code">
      <input class="field" style="left:231px;top:184px" placeholder="ZielAdresse Deutschland">
      <input class="field" style="left:21px;top:233px" placeholder="Wie Viele Kartons">
      <input class="field" style="left:232px;top:233px" placeholder="Karton Gewicht">
      <input class="field" style="left:21px;top:279px" placeholder="Abmessungen  L / W / H">
      <button class="send-btn" type="button">
        <svg width="18" height="18" viewBox="0 0 24 24" fill="none" stroke="#fff" stroke-width="1.5"><path d="M22 2L2 11l8 3 3 8z"/><path d="M22 2L10 14"/></svg>
        SENDEN
      </button>
    </form>
    <div class="quote-mark">“</div>
    <h2 class="reviews-title">Was under Kunde sagt</h2>
    <div class="review" style="left:153px">
      <p class="review-text">Schneller Versand - nur 4 Tage Laufzeit</p>
      <div class="reviewer" style="left:71px"><div class="avatar" role="img" aria-label="Porträtfoto eines Kunden"></div><div><div class="reviewer-name">Mirko Stahl</div><div class="stars">★★★★★</div></div></div>
    </div>
    <div class="review" style="left:456px">
      <p class="review-text">1A Service, ohne Probleme</p>
      <div class="reviewer" style="left:83px"><div class="avatar" role="img" aria-label="Porträtfoto eines Kunden"></div><div><div class="reviewer-name">Lukas Brede</div><div class="stars">★★★★★</div></div></div>
    </div>
    <div class="review" style="left:759px">
      <p class="review-text">Gute Preise - nur zu empfehlen.</p>
      <div class="reviewer" style="left:83px"><div class="avatar" role="img" aria-label="Porträtfoto eines Kunden"></div><div><div class="reviewer-name">Mirko Stahl</div><div class="stars">★★★★★</div></div></div>
    </div>
  </section>
  <footer class="footer">Copyright 2021. Alle Rechte vorbehalten.</footer>
</div>
</body>
</html>
```